Home Inspector

i do home inspections in Houston Texas. Would like a nice logo(maybe forest green and black). I inspect:foundations,structural,electric,plumbing,appliances,pools/spas and other optional systems.Hours mon-sat.

Contact Information for Business Card

BRIGHTWELL PROPERTY INSPECTIONS,5837 Tallow Creek,Houston,Texas,77268,Daniel Okafor,Professional Inspector,License#48726,Serving the Greater Houston Area

```html
<!DOCTYPE html>
<html lang="en">
<head>
<meta charset="utf-8">
<title>Brightwell Property Inspections – Business Card</title>
<link rel="stylesheet" href="https://fonts.googleapis.com/css2?family=Open+Sans:wght@400;600&display=swap">
<style>
  :root {
    --stage: #e9eaec;
    --card-dark: #0d0f11;
    --card-dark-edge: #1b1e22;
    --card-light: #ffffff;
    --brand-blue: #0f5ea8;
    --brand-blue-text: #1f63ad;
    --brand-green: #22a04a;
    --ink: #2a2a2a;
    --ink-light: #f2f2f2;
  }
  * { box-sizing: border-box; margin: 0; padding: 0; }
  html, body { width: 1200px; height: 750px; overflow: hidden; }
  body {
    background: var(--stage);
    font-family: "Open Sans", Arial, sans-serif;
    position: relative;
  }
  .card {
    position: absolute;
    top: 211px;
    width: 510px;
    height: 292px;
    border-radius: 24px;
    overflow: hidden;
  }

  /* Front: services */
  .card-front {
    left: 79px;
    background: radial-gradient(ellipse at 55% 40%, var(--card-dark-edge) 0%, var(--card-dark) 75%);
  }
  .brand-front {
    position: absolute;
    left: 48px;
    top: 104px;
    width: 200px;
    display: flex;
    align-items: center;
    gap: 10px;
  }
  .brand-mark {
    flex: 0 0 auto;
    width: 18px;
    height: 18px;
    background: var(--brand-green);
  }
  .brand-name {
    font-weight: 600;
    font-size: 19px;
    line-height: 1.2;
    letter-spacing: 0.5px;
  }
  .card-front .brand-name { color: var(--brand-green); }
  .front-divider {
    position: absolute;
    left: 275px;
    top: 72px;
    width: 2px;
    height: 148px;
    background: linear-gradient(to bottom, transparent, #2c3035 30%, #2c3035 70%, transparent);
  }
  .service-list {
    position: absolute;
    left: 299px;
    top: 82px;
    list-style: none;
    color: var(--ink-light);
    font-size: 17px;
    line-height: 20.5px;
    letter-spacing: 0.6px;
  }

  /* Back: contact */
  .card-back {
    left: 609px;
    background: var(--card-light);
  }
  .name-band {
    position: absolute;
    left: 0;
    top: 14px;
    width: 100%;
    height: 72px;
    background: var(--brand-blue);
    color: #fff;
    text-align: center;
    padding-top: 15px;
  }
  .person-name { font-size: 19px; line-height: 23px; letter-spacing: 0.4px; }
  .person-title { font-size: 14.5px; line-height: 18px; letter-spacing: 0.4px; }
  .brand-back {
    position: absolute;
    left: 48px;
    top: 142px;
    width: 170px;
    display: flex;
    align-items: center;
    gap: 10px;
  }
  .card-back .brand-name { color: var(--brand-blue-text); font-size: 17px; }
  .back-divider {
    position: absolute;
    left: 238px;
    top: 88px;
    width: 6px;
    height: 186px;
    background: linear-gradient(to bottom, rgba(0,0,0,0.05), rgba(0,0,0,0.28) 50%, rgba(0,0,0,0.02));
    filter: blur(1.5px);
  }
  .contact-details {
    position: absolute;
    left: 281px;
    top: 122px;
    font-size: 16.5px;
    line-height: 20.6px;
    letter-spacing: 0.4px;
    color: var(--ink);
  }
  .contact-label { color: var(--brand-blue-text); }
</style>
</head>
<body>

  <section class="card card-front" aria-label="Business card front">
    <div class="brand-front">
      <span class="brand-mark"></span>
      <span class="brand-name">BRIGHTWELL PROPERTY INSPECTIONS</span>
    </div>
    <div class="front-divider"></div>
    <ul class="service-list">
      <li>Electric</li>
      <li>Structural</li>
      <li>Plumbing</li>
      <li>Appliances</li>
      <li>Pools/spas</li>
      <li>Foundations</li>
      <li>Other optional systems</li>
    </ul>
  </section>

  <section class="card card-back" aria-label="Business card back">
    <header class="name-band">
      <p class="person-name">Daniel Okafor</p>
      <p class="person-title">Professional Inspector,License#48726</p>
    </header>
    <div class="brand-back">
      <span class="brand-mark"></span>
      <span class="brand-name">BRIGHTWELL PROPERTY INSPECTIONS</span>
    </div>
    <div class="back-divider"></div>
    <div class="contact-details">
      <p class="contact-label">Business Address:</p>
      <p>5837 Tallow Creek Dr</p>
      <p>Houston, TX 77268</p>
      <p class="contact-label">Business Hours:</p>
      <p>Mon-Sat by Appt</p>
    </div>
  </section>

</body>
</html>
```